Property management company looking for modern card design

We at Blue Maple Holdings provides property management services for its residential and commercial properties, with expertise in all categories of multifamily, industrial and office projects throughout California.

We need a business card design that is professional and modern designed business card. In our field, clients get hundreds of business cards, we would like our card to stand out.

Please avoid small print.

Target Market(s)

Professionals and high end clients

Industry/Entity Type

Financial Planning

Contact Information for Business Card

Company Name: Blue Maple Holdings, Name, email, license #, phone number, website bluemapleholdings.example

Font styles to use
Sans Serif

Requirements
Must have
• The card design needs to be adaptable because there is a possibly we will be expanding into different sectors other than real estate. The card design should be focused on financial planning and asset management.
Nice to have
• Modern and simple business card. Eye catching. Non-standard size/shaped cards would be great.
• bluemapleholdings.example
Should not have
• Too many bright color or any pictures or shapes of real estate stuff.

```html
<!DOCTYPE html>
<html lang="en">
<head>
<meta charset="utf-8">
<title>Blue Maple Holdings – Business Card</title>
<link rel="stylesheet" href="https://fonts.googleapis.com/css2?family=Inter:wght@300;400&family=Marcellus&display=swap">
<style>
  :root {
    --backdrop: #8e8e90;
    --kraft: #a88a5c;
    --kraft-edge: #9a7d50;
    --coral: #ee2233;
    --coral-deep: #b3142a;
    --ink: #1f1a14;
    --black: #111111;
  }
  * { margin: 0; padding: 0; box-sizing: border-box; }
  html, body {
    width: 1200px; height: 902px; overflow: hidden;
    background: var(--backdrop);
  }
  .card {
    position: absolute; left: 180px; top: 211px;
    width: 840px; height: 480px;
    background: var(--kraft);
    box-shadow: 0 10px 30px rgba(0,0,0,0.25);
    overflow: hidden;
    font-family: "Inter", Helvetica, Arial, sans-serif;
  }
  .brand {
    position: absolute; left: 40px; top: 70px; width: 360px;
    text-align: center;
  }
  .brand-dot {
    width: 130px; height: 130px; border-radius: 50%;
    background: var(--coral-deep);
    margin: 0 auto 34px;
  }
  .brand-name {
    font-family: "Marcellus", "Optima", serif;
    font-size: 28px; letter-spacing: 4px;
    color: var(--coral); text-transform: uppercase;
    line-height: 1.3;
  }
  .divider {
    position: absolute; left: 428px; top: 40px;
    width: 1.5px; height: 345px;
    background: var(--coral);
  }
  .holder-name {
    position: absolute; left: 460px; top: 52px;
    font-size: 36px; font-weight: 300; color: var(--coral);
  }
  .contacts {
    position: absolute; left: 462px; top: 196px;
    list-style: none;
  }
  .contacts li {
    display: flex; align-items: center;
    height: 50px;
    font-size: 24px; font-weight: 300; color: var(--ink);
  }
  .contact-icon {
    width: 32px; height: 32px; margin-right: 16px;
    background: var(--coral); border-radius: 4px;
    display: flex; align-items: center; justify-content: center;
    flex: none;
  }
  .rule-black {
    position: absolute; left: 0; top: 402px;
    width: 100%; height: 6px; background: var(--black);
  }
  .band-coral {
    position: absolute; left: 0; top: 408px;
    width: 100%; height: 72px; background: var(--coral);
  }
</style>
</head>
<body>
  <div class="card">
    <div class="brand">
      <div class="brand-dot"></div>
      <div class="brand-name">Blue Maple<br>Holdings</div>
    </div>

    <div class="divider"></div>

    <div class="holder-name">Dana Whitfield</div>

    <ul class="contacts">
      <li>
        <span class="contact-icon">
          <svg width="20" height="20" viewBox="0 0 20 20" aria-hidden="true">
            <path d="M3 7c0-2 2-3 7-3s7 1 7 3v1h-3V7H6v1H3z M5 9h10l1 7H4z" fill="#111"/>
            <circle cx="10" cy="12.5" r="2" fill="#ee2233"/>
          </svg>
        </span>
        555-014-2290
      </li>
      <li>
        <span class="contact-icon">
          <svg width="20" height="20" viewBox="0 0 20 20" aria-hidden="true">
            <rect x="2" y="5" width="16" height="11" fill="#111"/>
            <path d="M2 5l8 6 8-6" fill="none" stroke="#ee2233" stroke-width="1.4"/>
          </svg>
        </span>
        dana@bluemaple.example
      </li>
      <li>
        <span class="contact-icon">
          <svg width="20" height="20" viewBox="0 0 20 20" aria-hidden="true">
            <circle cx="10" cy="10" r="7.5" fill="none" stroke="#111" stroke-width="1.6"/>
            <ellipse cx="10" cy="10" rx="3.2" ry="7.5" fill="none" stroke="#111" stroke-width="1.3"/>
            <path d="M2.5 10h15M4 6h12M4 14h12" stroke="#111" stroke-width="1.2"/>
          </svg>
        </span>
        bluemapleholdings.example
      </li>
    </ul>

    <div class="rule-black"></div>
    <div class="band-coral"></div>
  </div>
</body>
</html>
```